New Technology Company is Launching New Products with a New Website

We want to create a 4-page website in WordPress compatible files to launch our site on HostMarrow. The attached files provide our ideas for Products, Services and About Us pages. We believe the content in those files is about right but the actual design is up to the artist that wants to accept this challenge. Additionally we need a fantastic Home page but we have no idea what that looks like. It obviously needs to lead to the other 3 pages but more importantly it needs to capture the interest of our current and future customers.

Details:
1. Please start off using the text descriptions in the example files. If shorter, longer, different descriptions are needed, just let us know.

2. Please feel free to suggest any photos you can find from free or reasonable stock photo services. Pixelgrove and others like them are reasonable. If you find a perfect image, please send us a link and we will buy a license if its affordable. I have paid ~US$10 per image in the past.

3. I have also uploaded our stationery and logo files. We would like the website design to be consistent with the logo and stationery designs. The stationery designs are all in one file.

We have two logos, and would like to see both of them used on the website. One logo shows the letters KRVT in an outlined shield that is read and blue. That logo is used in the stationery and in our draft website design as a header. The other logo shows flames bouncing off a round shield. Perhaps this logo could be used at the bottom of each page on the website, or some other place where it would be fun and creative without diminishing the seriousness of our underlying science and engineering.

4. We are looking for an artist to have some fun with this and propose something creative. We have lots of boring ideas ourselves so we need YOU to do something else! Thank you so much for considering this challenge!

Target Market(s)

People interested in new, high performance fabrics, including consumers, store owners, garment designers and companies like Brindlecrest or Quillon Outfitters

Coding

Coded - Design and coding required

Font styles to use
Sans Serif

Colors
f04a51
3277b5

Requirements
Must have
• something unforgetable

```html
<!DOCTYPE html>
<html lang="en">
<head>
<meta charset="utf-8">
<title>KRVT – High Performance Fabrics</title>
<link rel="stylesheet" href="https://fonts.googleapis.com/css2?family=Roboto:wght@400;500;700&family=Open+Sans:wght@400;600&display=swap">
<style>
:root{
  --red:#f04a51;
  --deep-red:#c8101d;
  --blue:#3277b5;
  --deep-blue:#1466b0;
  --ink:#1d1d1d;
  --body:#5a5a5a;
  --white:#ffffff;
  --rule:#d9d9d9;
}
*{margin:0;padding:0;box-sizing:border-box}
html,body{width:1200px;height:3442px;overflow:hidden;background:var(--white)}
body{position:relative;font-family:"Open Sans",Arial,sans-serif;color:var(--body)}
.abs{position:absolute}
.hero{left:0;top:0;width:1200px;height:615px;background:linear-gradient(180deg,#3a2418 0%,#8a3a17 30%,#c2581d 50%,#6b3520 75%,#2a221f 100%)}
.hero-glow{left:0;top:0;width:1200px;height:615px;background:radial-gradient(ellipse 520px 300px at 800px 200px,rgba(255,150,40,.55),transparent 70%),radial-gradient(ellipse 300px 200px at 250px 300px,rgba(255,120,30,.35),transparent 70%)}
.topbar{left:0;top:0}
.brand{left:118px;top:28px;font-family:"Roboto",Arial,sans-serif;font-weight:700;font-size:40px;color:var(--white);letter-spacing:1px;display:flex;align-items:center;gap:12px}
.brand-mark{width:26px;height:26px;background:var(--red)}
.call{right:114px;top:14px;font-family:"Roboto",Arial,sans-serif;font-weight:700;font-size:18px;color:var(--white);display:flex;align-items:center;gap:8px}
.nav{right:114px;top:55px;display:flex;gap:36px;font-family:"Roboto",Arial,sans-serif;font-weight:500;font-size:16px;color:var(--white)}
.hero-title{left:117px;top:218px;font-family:"Roboto",Arial,sans-serif;font-weight:700;font-size:66px;color:var(--white)}
.hero-copy{left:117px;top:302px;width:400px;font-size:15.5px;line-height:27px;color:var(--white)}
.hero-btn{left:117px;top:415px;width:158px;height:53px;border:2px solid var(--white);color:var(--white);font-family:"Roboto",Arial,sans-serif;font-weight:700;font-size:15px;display:flex;align-items:center;justify-content:center}
.sec-title{font-family:"Roboto",Arial,sans-serif;font-weight:400;font-size:34px;line-height:42px;color:var(--ink)}
.sec-copy{font-size:17px;line-height:24px;color:var(--body)}
.sec-copy p{margin-bottom:22px}
.small{font-size:15px;line-height:26px}
.light{color:var(--white)}
.photo{border:0}
.footer-col h4{font-family:"Roboto",Arial,sans-serif;font-weight:500;font-size:19px;color:var(--ink);margin-bottom:16px}
.footer-col li{list-style:none;font-size:12.5px;line-height:25.5px;color:#444}
.footer-col{padding-left:18px;border-left:1px solid var(--rule);height:205px}
.foot-brand{left:136px;top:3170px;display:flex;align-items:center;gap:12px;font-family:"Roboto",Arial,sans-serif;font-weight:700;font-size:40px;color:var(--deep-blue)}
.foot-brand span.dot{width:30px;height:30px;border-radius:50%;background:var(--red)}
.copyright{left:112px;top:3380px;font-size:12px;color:#444}
.social{right:120px;top:3366px;display:flex;gap:12px}
.social span{width:36px;height:36px;border-radius:50%;border:1.5px solid var(--deep-blue)}
.footer-rule{left:112px;top:3348px;width:976px;height:1px;background:var(--rule)}
svg text{font-family:"Open Sans",Arial,sans-serif}
</style>
</head>
<body>

<div class="abs hero" role="img" aria-label="Firefighters spraying water on a burning building surrounded by smoke"></div>
<div class="abs hero-glow"></div>
<svg class="abs topbar" width="1200" height="100" viewBox="0 0 1200 100" aria-hidden="true">
  <path d="M0 0H1200V92C1050 84 900 86 600 98C420 102 300 40 0 66Z" fill="var(--deep-blue)"/>
</svg>
<div class="abs brand"><span class="brand-mark"></span>KRVT</div>
<div class="abs call">
  <svg width="16" height="16" viewBox="0 0 24 24" aria-hidden="true"><path fill="#fff" d="M6.6 10.8a15.1 15.1 0 0 0 6.6 6.6l2.2-2.2c.3-.3.7-.4 1-.2 1.1.4 2.3.6 3.6.6.6 0 1 .4 1 1V20c0 .6-.4 1-1 1A17 17 0 0 1 3 4c0-.6.4-1 1-1h3.5c.6 0 1 .4 1 1 0 1.3.2 2.5.6 3.6.1.3 0 .7-.2 1z"/></svg>
  Call us:&nbsp; 928-555-0142
</div>
<nav class="abs nav"><span>PRODUCTS</span><span>SERVICES</span><span>ABOUT US</span><span>CONTACT US</span></nav>
<h1 class="abs hero-title">KRVT</h1>
<p class="abs hero-copy">Neque porro quisquam est, qui dolorem ipsum quia dolor sit amet, consectetur, adipisci velit, sed quianon numquam eius modi tempor.</p>
<div class="abs hero-btn">GET MORE INFO</div>

<h2 class="abs sec-title" style="left:126px;top:710px;width:360px">High – Temperature Insulation</h2>
<div class="abs sec-copy" style="left:124px;top:822px;width:440px">
  <p>KRVT has been working on aerospace applications of high temperature insulations since the National Aerospace Plane was proposed by Harlan Whitcombe.</p>
  <p>Back then we used gold and platinum to block heat. Today we make insulations that are much more affordable, much more efficient and more reliable in Thermal Protection Systems.</p>
  <p>If this is what you need, contact us and ask about our Opacified Fibrous Insulation (OFI).</p>
</div>
<div class="abs photo" style="left:643px;top:695px;width:422px;height:200px;background:linear-gradient(180deg,#0c0c0c 0%,#6e1418 35%,#c8282c 48%,#e8dcc8 60%,#1c1a18 100%)" role="img" aria-label="Red heat-shield dome glowing above a white frame in a test chamber"></div>
<svg class="abs" style="left:630px;top:925px" width="450" height="240" viewBox="0 0 450 240" aria-label="Line chart of two insulation curves">
  <g fill="#1466b0" font-size="13">
    <text x="30" y="34" text-anchor="end">2.0</text><text x="30" y="79" text-anchor="end">1.5</text>
    <text x="30" y="124" text-anchor="end">1.0</text><text x="30" y="169" text-anchor="end">0.5</text>
    <text x="30" y="214" text-anchor="end">0.0</text>
    <text x="76" y="236" text-anchor="middle">500</text><text x="135" y="236" text-anchor="middle">1000</text>
    <text x="194" y="236" text-anchor="middle">1500</text><text x="253" y="236" text-anchor="middle">2000</text>
    <text x="312" y="236" text-anchor="middle">2500</text><text x="371" y="236" text-anchor="middle">3000</text>
  </g>
  <line x1="40" y1="210" x2="430" y2="210" stroke="#1466b0" stroke-width="1.5"/>
  <path d="M45 168C150 150 250 130 330 90S410 30 430 15" fill="none" stroke="#d0141e" stroke-width="3"/>
  <path d="M135 210C200 205 260 195 320 175S405 115 432 95" fill="none" stroke="#1466b0" stroke-width="3"/>
</svg>

<svg class="abs" style="left:0;top:1245px" width="1200" height="700" viewBox="0 0 1200 700" aria-hidden="true">
  <defs><linearGradient id="bandBlue" x1="0" y1="0" x2="0" y2="1"><stop offset="0" stop-color="#1772c0"/><stop offset="1" stop-color="#0f5fa6"/></linearGradient></defs>
  <polygon points="0,28 520,22 0,55" fill="var(--deep-red)"/>
  <polygon points="0,45 1200,8 1200,640 0,682" fill="url(#bandBlue)"/>
  <polygon points="760,648 1200,628 1200,660" fill="var(--deep-red)"/>
</svg>
<div class="abs photo" style="left:156px;top:1368px;width:424px;height:199px;background:linear-gradient(180deg,#a9c6df 0%,#dfe8ef 35%,#7a8a7c 65%,#4b5a46 100%)" role="img" aria-label="Hiker with a backpack on a mountain trail overlooking a valley"></div>
<svg class="abs" style="left:140px;top:1583px" width="460" height="260" viewBox="0 0 460 260" aria-label="Bar chart comparing warmth of insulation materials">
  <g fill="#fff" font-size="12">
    <text x="36" y="20" text-anchor="end">50</text><text x="36" y="57" text-anchor="end">40</text>
    <text x="36" y="95" text-anchor="end">30</text><text x="36" y="133" text-anchor="end">20</text>
    <text x="36" y="171" text-anchor="end">10</text><text x="36" y="209" text-anchor="end">0</text>
  </g>
  <g stroke="rgba(255,255,255,.35)" stroke-width="1">
    <line x1="46" y1="16" x2="445" y2="16"/><line x1="46" y1="53" x2="445" y2="53"/>
    <line x1="46" y1="91" x2="445" y2="91"/><line x1="46" y1="129" x2="445" y2="129"/>
    <line x1="46" y1="167" x2="445" y2="167"/>
  </g>
  <line x1="46" y1="205" x2="445" y2="205" stroke="#fff" stroke-width="1.5"/>
  <rect x="66" y="61" width="34" height="144" fill="#2a8ee0"/>
  <rect x="151" y="110" width="34" height="95" fill="#d0141e"/>
  <rect x="236" y="148" width="34" height="57" fill="#6bc22a"/>
  <rect x="322" y="38" width="34" height="167" fill="#0b3b6e"/>
  <rect x="407" y="16" width="34" height="189" fill="#45c0ea"/>
  <g fill="#fff" font-size="11" text-anchor="middle">
    <text x="83" y="223">Goose</text><text x="83" y="236">Down</text>
    <text x="168" y="223">PET</text><text x="168" y="236">FIBER</text>
    <text x="253" y="223">WOOL</text><text x="253" y="236">FELT</text>
    <text x="339" y="223">AEROGEL</text><text x="339" y="236">INSULATION</text>
    <text x="424" y="223">KRVT</text><text x="424" y="236">FRIA</text>
  </g>
</svg>
<h2 class="abs sec-title light" style="left:650px;top:1363px">Aerogel Insulations</h2>
<div class="abs sec-copy light" style="left:650px;top:1425px;width:395px;font-size:18px;line-height:24.5px">
  <p>KRVT has developed aerogel insulations that are thin, flexible and more than twice as warm as goose down.&nbsp; Although we developed these insulations for ORBITA to take payloads to Mars, we are very excited about their more earthly applications from cold weather clothing to industrial pipelines.</p>
  <p>If this is what you need, contact us and ask about our Fiber Reinforced Insulation with Aerogel (FRIA).</p>
</div>

<h2 class="abs sec-title" style="left:131px;top:2010px">Fire Resistant Fabrics</h2>
<div class="abs sec-copy small" style="left:131px;top:2060px;width:455px">
  <p>KRVT developed fire resistant fabrics and insulation blankets that provide various levels of protection for fire fighters surviving a burn over.&nbsp; The current K-Shield 20 fire shelter has saved many lives and prevented many injuries, but the tragic loss of 19 Cedar Ridge Hot Shots in 2013 motivated us to develop better fire shelters for today’s wild fires that burn hotter and longer than those of 20 years ago.</p>
  <p>If this is what you need, contact us and ask for the KRVT 1080/7, KRVT S/7 and KRVT MLI fabrics.</p>
</div>
<div class="abs photo" style="left:652px;top:2003px;width:420px;height:196px;background:linear-gradient(180deg,#2a2a2c 0%,#c46a1c 30%,#f0a02a 50%,#9a3a12 70%,#3a3a3e 100%)" role="img" aria-label="Large fuel fire with responders spraying foam"></div>
<svg class="abs" style="left:660px;top:2213px" width="410" height="245" viewBox="0 0 410 245" aria-label="Calorimeter test line chart per ISO 9151:1995">
  <text x="205" y="19" text-anchor="middle" font-size="17" fill="#1d1d1d">Calorimeter Test Per ISO: 9151:1995</text>
  <g fill="#1466b0" font-size="11">
    <text x="24" y="45" text-anchor="end">60</text><text x="24" y="75" text-anchor="end">50</text>
    <text x="24" y="105" text-anchor="end">40</text><text x="24" y="135" text-anchor="end">30</text>
    <text x="24" y="165" text-anchor="end">20</text><text x="24" y="195" text-anchor="end">10</text>
    <text x="24" y="225" text-anchor="end">0</text>
  </g>
  <line x1="30" y1="34" x2="30" y2="222" stroke="#888" stroke-width="1"/>
  <line x1="30" y1="222" x2="395" y2="222" stroke="#888" stroke-width="1"/>
  <g fill="#1466b0" font-size="10" text-anchor="middle">
    <text x="33" y="238">0</text><text x="59" y="238">5</text><text x="85" y="238">10</text><text x="111" y="238">15</text>
    <text x="137" y="238">20</text><text x="163" y="238">25</text><text x="189" y="238">30</text><text x="215" y="238">35</text>
    <text x="241" y="238">40</text><text x="267" y="238">45</text><text x="293" y="238">50</text><text x="319" y="238">55</text>
    <text x="345" y="238">60</text><text x="371" y="238">65</text><text x="397" y="238">70</text>
  </g>
  <path d="M40 222C80 215 110 200 130 170S175 80 205 38" fill="none" stroke="#d0141e" stroke-width="2"/>
  <path d="M50 222C100 215 135 200 160 172S215 85 250 38" fill="none" stroke="#f07a1e" stroke-width="2"/>
  <path d="M60 222C115 215 160 200 190 172S255 90 295 40" fill="none" stroke="#2e9a3a" stroke-width="2"/>
  <path d="M70 222C130 218 185 205 220 178S300 95 345 42" fill="none" stroke="#1a3aa8" stroke-width="2"/>
</svg>

<svg class="abs" style="left:0;top:2505px" width="1200" height="590" viewBox="0 0 1200 590" aria-hidden="true">
  <polygon points="700,22 1200,6 1200,34" fill="var(--deep-blue)"/>
  <polygon points="0,28 1200,20 1200,540 0,565" fill="var(--deep-red)"/>
  <polygon points="0,560 420,555 0,580" fill="var(--deep-blue)"/>
</svg>
<div class="abs photo" style="left:174px;top:2639px;width:434px;height:326px;background:linear-gradient(180deg,#9cbfd2 0%,#d9e4e8 40%,#5d6f5a 70%,#3a4538 100%)" role="img" aria-label="Time-trial cyclist in aero suit and helmet with labels showing seconds saved by each aerodynamic upgrade"></div>
<h2 class="abs sec-title light" style="left:652px;top:2668px">Aerodynamic Fabrics</h2>
<div class="abs sec-copy light" style="left:652px;top:2728px;width:400px;font-size:18px;line-height:24.5px">
  <p>KRVT developed and patented aerodynamic fabrics, and measured the drag reduction on bicycles in a wind tunnel.</p>
  <p>If you need to go faster or reduce energy costs, contact us about our Slipstream Weave fabric</p>
</div>

<div class="abs foot-brand"><span class="dot"></span>KRVT</div>
<div class="abs footer-col" style="left:434px;top:3128px;width:200px;border-left:0">
  <h4>INFORMATION</h4>
  <ul><li>About Us</li><li>Careers</li><li>Privacy &amp; Security</li><li>Site Map</li><li>Terms of Use</li><li>Blog</li></ul>
</div>
<div class="abs footer-col" style="left:636px;top:3128px;width:230px">
  <h4>HELP &amp; SUPPORT</h4>
  <ul><li>Recommended Reading</li><li>Submit your Story</li><li>Contact Us</li><li>Frequently Asked Questions</li><li>How to Order</li></ul>
</div>
<div class="abs footer-col" style="left:884px;top:3128px;width:230px">
  <h4>MY ACCOUNT</h4>
  <ul><li>Delivery Information</li><li>My Account</li><li>Order Tracking</li><li>Reminder Service</li><li>Shipping, Returns &amp; Fees</li></ul>
</div>
<div class="abs footer-rule"></div>
<p class="abs copyright">Copyright © 2018, KRVT. All Rights Reserved.</p>
<div class="abs social" aria-label="Social links"><span></span><span></span><span></span><span></span></div>

</body>
</html>
```